Zielgruppe
Ich suche nach einem Design für ein Buchcover. Zielgruppe sind Leser/innen von historischen Liebesromanen, circa 30 Jahre aufwärts.
Aufgabenstellung
Inhalt und Design:
Bei dem Roman 'Der Fächer' von Mara Quentel, handelt es sich um einen historischen Liebesroman, der hauptsächlich in Paris spielt. (siehe Anhang Klappentext und Exposé zur Erläuterung der Geschichte). Daher wäre die grobe Idee, den Eiffelturm als Symbol für Paris auf dem Cover zu haben und auch das Thema des Titels 'Der Fächer' darzustellen. In der Geschichte steht ein 60 Jahre alter Liebesbrief (aus den 20er Jahren) im Mittelpunkt des Geschehens. Daher sollte das Thema Brief auf dem Cover aufgenommen werden, dies kann in Form von reinem handschriftlichen Text sein, der sich transparent über das ganze Cover zieht (siehe mockup im Anhang) oder in Form eines Briefes, der beispielsweise auf einem Cafétisch in einem Pariser Café liegt. Der Fächer muss auf jeden Fall handgeschrieben sein und in einer Schrift, die an früher erinnert.
Stil:
Vom Stil her sollte es nicht nach kitschigem Liebesroman aussehen, sondern eleganter und dezenter. Farblich würde ich nicht zu grelle Farben wählen, wie gelb oder rot, sondern mehr in einem pastelligen Bereich bleiben, es muss nicht unbedingt blau sein, wie im Mockup, sondern sollte möglichst das Zielpublikum ansprechen. Das Design kann sowohl auf Fotos basieren als auch auf stilistischen Zeichnungen - hier ist der Designer frei.
UPDATE: Es sollte nicht unbedingt monochrom sein, auch nicht sepia oder brauntöne, schon Farben, die Aufmerksamkeit erregen!
UPDATE: Das Cover muss nicht so sein, wie in dem Mockup, das war nur eine Idee...es kann auch anders gestaltet werden, mit dem Brief auf einen Tisch in eine Cafe, oder ganz anders.
Technische Vorgaben:
Auf der Rückseite soll der Klappentext eingefügt werden.
Das Buchcover Design muss für Velnor TSQ Print und ebook verwendbar sein.
Das Design darf nicht zu überladen sein.

```html
<!DOCTYPE html>
<html lang="de">
<head>
<meta charset="utf-8">
<title>Der Fächer – Mara Quentel</title>
<link rel="stylesheet" href="https://fonts.googleapis.com/css2?family=Special+Elite&family=Allura&display=swap">
<style>
  :root {
    --orchid: #d564d2;
    --orchid-deep: #c24fc3;
    --paper: #efe6cc;
    --paper-shade: #ddd0ad;
    --ink: #111111;
    --script-ink: #5d4a60;
    --tower-tone: rgba(255, 226, 250, 0.55);
  }
  html, body {
    margin: 0;
    padding: 0;
    overflow: hidden;
    background: #ffffff;
  }
  .cover {
    position: relative;
    width: 848px;
    height: 1200px;
    overflow: hidden;
    background: linear-gradient(180deg, var(--orchid) 0%, var(--orchid-deep) 60%, var(--orchid) 100%);
  }
  .paper-layer {
    position: absolute;
    inset: 0;
  }
  .tower-illustration {
    position: absolute;
    left: 0;
    top: 138px;
    width: 345px;
    height: 1062px;
  }
  .title-block {
    position: absolute;
    right: 86px;
    top: 58px;
    text-align: right;
    font-family: "Special Elite", "Courier New", monospace;
    color: var(--ink);
  }
  .author {
    margin: 0;
    font-size: 38px;
    line-height: 1;
    letter-spacing: 1px;
  }
  .title {
    margin: 6px 0 0;
    font-size: 70px;
    line-height: 1;
    font-weight: 700;
    letter-spacing: 2px;
  }
  .address {
    position: absolute;
    left: 538px;
    top: 188px;
    font-family: "Allura", cursive;
    font-size: 40px;
    line-height: 46px;
    color: var(--script-ink);
    opacity: 0.7;
  }
  .letter-text {
    position: absolute;
    left: 0;
    top: 643px;
    width: 848px;
    height: 557px;
    overflow: hidden;
    margin: 0;
    text-align: center;
    font-family: "Allura", cursive;
    font-size: 29px;
    line-height: 32px;
    color: var(--script-ink);
  }
  .letter-text p {
    margin: 0 0 14px;
  }
</style>
</head>
<body>
<main class="cover">
  <svg class="paper-layer" width="848" height="1200" viewBox="0 0 848 1200" aria-hidden="true">
    <defs>
      <linearGradient id="paperFade" x1="0" y1="0" x2="1" y2="0">
        <stop offset="0" stop-color="#efe6cc" stop-opacity="0.15"/>
        <stop offset="0.35" stop-color="#efe6cc" stop-opacity="0.9"/>
        <stop offset="1" stop-color="#efe6cc"/>
      </linearGradient>
      <linearGradient id="paperBottomFade" x1="0" y1="0" x2="0" y2="1">
        <stop offset="0" stop-color="#e8ddc0"/>
        <stop offset="1" stop-color="#e8ddc0" stop-opacity="0"/>
      </linearGradient>
    </defs>
    <polygon class="torn-paper" fill="url(#paperFade)"
      points="213,40 250,34 290,38 330,30 372,36 410,28 455,34 500,26 545,32 590,24 635,30 680,22 725,28 770,24 812,30 848,26 848,455 810,450 770,456 730,448 690,454 650,446 612,452 575,444 540,448 515,440 513,380 520,330 360,280 213,250"/>
    <polygon class="torn-strip" fill="url(#paperBottomFade)"
      points="0,598 60,596 120,594 200,592 300,590 360,584 390,566 420,560 450,570 480,580 540,584 620,580 700,578 780,574 848,572 848,590 760,594 680,598 600,600 520,602 440,600 360,604 280,602 200,604 120,606 60,606 0,608"/>
  </svg>

  <svg class="tower-illustration" viewBox="0 0 345 1062" role="img" aria-label="Stilisierte Zeichnung des Eiffelturms in hellem Rosa">
    <defs>
      <linearGradient id="towerTone" x1="0" y1="0" x2="0" y2="1">
        <stop offset="0" stop-color="#ffe2fa" stop-opacity="0.35"/>
        <stop offset="1" stop-color="#ffe2fa" stop-opacity="0.6"/>
      </linearGradient>
    </defs>
    <rect width="345" height="1062" fill="url(#towerTone)"/>
  </svg>

  <header class="title-block">
    <p class="author">Mara Quentel</p>
    <h1 class="title">Der Fächer</h1>
  </header>

  <div class="address">
    <div>Odile</div>
    <div>Rue</div>
    <div>Pa</div>
  </div>

  <section class="letter-text">
    <p>Lorem ipsum dolor sit amet, consectetur adipisici elit, sed eiusmod tempor incidunt ut labore et dolore magna aliqua. Ut enim ad minim veniam, quis nostrud exercitation ullamco laboris nisi ut aliquid ex ea commodi consequat. Quis aute iure reprehenderit in voluptate velit esse cillum dolore eu fugiat nulla pariatur. Excepteur sint obcaecat cupiditat non proident, sunt in culpa qui officia deserunt mollit anim id est laborum.</p>
    <p>Duis autem vel eum iriure dolor in hendrerit in vulputate velit esse molestie consequat, vel illum dolore eu feugiat nulla facilisis at vero eros et accumsan et iusto odio dignissim qui blandit praesent luptatum zzril delenit augue duis dolore te feugait nulla facilisi. Lorem ipsum dolor sit amet, consectetuer adipiscing elit, sed diam nonummy nibh euismod tincidunt ut laoreet dolore magna aliquam erat volutpat. Ut wisi enim ad minim veniam, quis nostrud exerci tation ullamcorper suscipit lobortis nisl ut aliquip ex ea commodo consequat. Duis autem vel eum iriure dolor in hendrerit in vulputate velit esse molestie consequat, vel illum dolore eu feugiat nulla facilisis at vero eros et accumsan et iusto odio dignissim qui blandit praesent luptatum zzril delenit augue duis dolore te feugait nulla facilisi.
    Nam liber tempor cum soluta nobis eleifend option congue nihil imperdiet doming id quod mazim placerat facer possim assum. Lorem ipsum dolor sit amet, consectetuer adipiscing elit, sed diam nonummy nibh euismod tincidunt ut laoreet dolore magna</p>
  </section>
</main>
</body>
</html>
```